Summer Sunglass offer

Need a poster design for a spring / summer campaign. We are an opticians with good footfall. The design needs to be eye catching and aimed at 40 year old plus. The offer is Up to 50% off sunglass offer, t&c apply. (I have attached our last year campaign)
Also need a 2 sided A5 leaflet design (see attached)
I've uploaded a copy of our logo

A5 leaflet should read:

Grab a bargain on two great looks this summer Upto 50% off sunglasses
Look great and stay safe in the sun this summer

We want you to look great, feel fantastic and most of all stay safe in the sun this summer. That’s why we’re offering you 50% off prescription sunglasses with every complete pair of glasses you buy this summer or 25% off for prescription sunglasses with no other purchase.
Find you new summer looks from our gorgeous collection of frames in store. It matters to us that you look great in your new glasses as much as how well you see through them, so we’ll be on hand to help you find frames that suit you best.
What new looks will you go for? Smart or sassy? Formal or Fun? Whatever you’re in the mood for, you’ll find it in our collections this summer.
Call in today to find your new looks, and remember to bring your prescription if you don’t need an eye test.

Target Market(s)

40 + year old

Industry/Entity Type

Optician

Colors

Designer to choose colors to be used in the design.

Requirements
Must have
• Images, preferably a male and Female image

```html
<!DOCTYPE html>
<html lang="en">
<head>
<meta charset="utf-8">
<title>Summer Sunglasses Offer – Elmbridge Eyecare Centre</title>
<link rel="stylesheet" href="https://fonts.googleapis.com/css2?family=Lato:wght@300;400;700&display=swap">
<style>
  :root {
    --offer-red: #e0234a;
    --hero-red-light: #ec3556;
    --hero-red-deep: #c3163a;
    --band-shade: rgba(140, 12, 36, 0.55);
    --ink: #3a3a3a;
    --muted: #8a8a8a;
    --rule-navy: #2b4c8c;
    --brand-teal: #2a9fa8;
    --paper: #ffffff;
  }
  html, body {
    margin: 0;
    padding: 0;
    background: var(--paper);
    overflow: hidden;
  }
  .leaflet {
    position: relative;
    width: 851px;
    height: 1200px;
    overflow: hidden;
    background: var(--paper);
    font-family: "Lato", "Helvetica Neue", Arial, sans-serif;
    color: var(--ink);
  }
  .hero {
    position: absolute;
    left: 0; top: 0;
    width: 851px;
    height: 505px;
    background: radial-gradient(ellipse at 50% 45%, var(--hero-red-light) 0%, var(--offer-red) 45%, var(--hero-red-deep) 100%);
  }
  .headline-band {
    position: absolute;
    left: 0; top: 0;
    width: 851px;
    height: 168px;
    background: var(--band-shade);
    color: var(--paper);
    text-align: center;
    text-transform: uppercase;
    font-size: 25px;
    line-height: 31px;
    font-weight: 400;
    padding-top: 12px;
    box-sizing: border-box;
    letter-spacing: 0.2px;
  }
  .headline-band p { margin: 0; }
  .headline-band .offer { font-weight: 700; }
  .body-copy {
    position: absolute;
    left: 88px;
    top: 528px;
    width: 690px;
    font-size: 22.5px;
    line-height: 32.5px;
    font-weight: 400;
  }
  .body-copy p { margin: 0 0 31px; }
  .body-copy strong { font-weight: 700; }
  .body-copy .call-to-action { color: var(--offer-red); margin: 0; }
  .rule {
    position: absolute;
    left: 0; top: 1035px;
    width: 851px;
    height: 7px;
    background: var(--rule-navy);
  }
  .brand {
    position: absolute;
    left: 44px;
    top: 1080px;
    display: flex;
    align-items: center;
    gap: 16px;
  }
  .brand-dot {
    width: 54px;
    height: 54px;
    border-radius: 50%;
    background: var(--brand-teal);
  }
  .brand-name {
    font-size: 27px;
    line-height: 30px;
    font-weight: 700;
    color: var(--brand-teal);
    text-transform: uppercase;
    letter-spacing: 1px;
  }
  .contact {
    position: absolute;
    left: 464px;
    top: 1072px;
    font-size: 20.5px;
    line-height: 28.5px;
    font-weight: 300;
    color: var(--muted);
  }
  .contact p { margin: 0; }
  .contact .web { color: var(--rule-navy); font-weight: 400; }
</style>
</head>
<body>
<main class="leaflet">
  <div class="hero" role="img" aria-label="Photo of a surprised woman in round sunglasses and a hat, hands to her cheeks, on a bright red background"></div>

  <header class="headline-band">
    <p>Grab a bargain on two great looks this summer</p>
    <p class="offer">Upto 50% off sunglasses.</p>
    <p>Look great and stay safe in the sun this summer.</p>
  </header>

  <section class="body-copy">
    <p>We want you to look great, feel fantastic and most of all stay safe in the sun this summer. That’s why we’re offering you <strong>50</strong>% off prescription sunglasses with every complete pair of glasses you buy this summer or <strong>25</strong>% off for prescription sunglasses with no other purchase.</p>
    <p>Find you new summer looks from our gorgeous collection of frames in store. It matters to us that you love how you look in your new glasses as much as how well you see through them, so we’ll be on hand to help you find frames that suit you best. What new looks will you go for? Smart or sassy? Formal or Fun? Whatever you’re in the mood for, you’ll find it in our collections this summer.</p>
    <p class="call-to-action">Call in today to find your new looks, and remember to bring your prescription if you don’t need an eye test.</p>
  </section>

  <div class="rule"></div>

  <footer>
    <div class="brand">
      <div class="brand-dot"></div>
      <div class="brand-name">Elmbridge<br>Eyecare Centre</div>
    </div>
    <address class="contact">
      <p>42 Market Row, Elmbridge, EL4 2QA.</p>
      <p>T: 01632960418</p>
      <p>e: info@elmbridgeeyecare.co.uk</p>
      <p class="web">elmbridgeeyecare.co.uk</p>
    </address>
  </footer>
</main>
</body>
</html>
```